VEMRA - new private security company in Guyana, South America needs a website & logo design

New private security company in Guyana needs a website ready for the company launch. The business will offer armed and unarmed security to high net worth individuals, politicians, government officials, diplomats and off-shore oil industry vessels and platforms.

The company has its own heliport and indoor training range, armoured vehicles, ambulances and uniformed security personnel, and we would like some imager to indicate this.

The team leaders are all ex-special forces.

The website structure should be something like:

PAGE 1 Home
PAGE 2 About Us
PAGE 3 Guyana Security Overview
PAGE 4 Services
PAGE 5 Contact Us
PAGE 6 Useful Links

We have uploaded a file with the text copy for each of these pages.

The web domain has been registered through Pellnet and is www.vemra.group

Target Market(s)

Corporations involved in the oil and gas industry, Embassies, Investment companies and individuals, Caribbean diaspora.

Industry/Entity Type

Security Service

Logo Text

VEMRA

Coding

Coded - Design and coding required

Number of Pages Required

5+ page

Font styles to use
Sans Serif

Requirements
Must have
• Must have:
an enquiry/contact form page
general location map: https://mapfold.example/loc/Kp82wQzLr5Ynb7Xh4;
text as per web content document uploaded to this site
Nice to have
• Images of private security (cars, bodyguards, helicopters/planes, etc)
Images of Maritime security (non-military)
Images of people of colour (Guyana has mainly afro and indian residents)
Image of a high tec security control room

```html
<!DOCTYPE html>
<html lang="en">
<head>
<meta charset="utf-8">
<title>VEMRA Security – About Us</title>
<link href="https://fonts.googleapis.com/css2?family=Oswald:wght@400;500;600&family=Lato:wght@400;700&display=swap" rel="stylesheet">
<style>
  :root{
    --canvas:#ffffff;
    --black:#000000;
    --charcoal:#252624;
    --blue:#2b7bbf;
    --blue-soft:#3d86c6;
    --hero-a:#3f5f82;
    --hero-b:#6d8fb3;
    --white:#ffffff;
    --rule:#3a3a3a;
  }
  *{margin:0;padding:0;box-sizing:border-box}
  html,body{width:1200px;height:1200px;overflow:hidden;background:var(--canvas)}
  body{position:relative;font-family:'Lato',sans-serif;color:var(--white)}
  .page{position:absolute;left:227px;top:32px;width:745px;height:1136px;background:var(--charcoal);overflow:hidden}

  /* header */
  .site-header{position:absolute;left:0;top:0;width:745px;height:44px;background:var(--black)}
  .brand{position:absolute;left:70px;top:6px;line-height:1}
  .brand-name{font-family:'Oswald',sans-serif;font-weight:600;font-size:19px;color:var(--white);display:block}
  .brand-tag{font-family:'Oswald',sans-serif;font-size:8px;letter-spacing:2.2px;color:var(--blue);display:block;margin-top:1px}
  .main-nav{position:absolute;right:108px;top:15px;display:flex;gap:22px;font-family:'Oswald',sans-serif;font-size:8px;font-weight:500}
  .main-nav a{color:var(--white);text-decoration:none}
  .main-nav a.is-active{color:var(--blue-soft)}

  /* page title band */
  .page-hero{position:absolute;left:0;top:44px;width:745px;height:96px;background:linear-gradient(90deg,var(--hero-a),var(--hero-b) 55%,var(--hero-a))}
  .page-title{position:absolute;left:0;width:100%;top:8px;text-align:center;font-family:'Oswald',sans-serif;font-weight:500;font-size:52px;line-height:1.1}
  .title-rule{position:absolute;left:351px;top:70px;width:44px;height:2px;background:var(--white)}

  /* intro */
  .intro-heading{position:absolute;left:70px;top:192px;width:300px;font-family:'Oswald',sans-serif;font-weight:500;font-size:20px;line-height:23px;text-transform:uppercase}
  .intro-copy{position:absolute;left:70px;top:268px;width:302px;font-size:8.7px;line-height:13px;font-weight:700}
  .intro-copy p{margin-bottom:15px}
  .intro-photo{position:absolute;left:417px;top:140px;width:328px;height:470px;background:linear-gradient(160deg,#3c4f60 0%,#1f2a33 55%,#141b22 100%)}

  /* assets */
  .section-title{position:absolute;left:0;width:100%;top:634px;text-align:center;font-family:'Oswald',sans-serif;font-size:28px;line-height:1}
  .section-rule{position:absolute;left:351px;top:677px;width:44px;height:2px;background:var(--blue)}
  .asset-card{position:absolute;top:716px;width:140px;height:144px;border-radius:4px;overflow:hidden;background:var(--blue)}
  .asset-image{height:111px}
  .asset-label{height:33px;display:flex;align-items:center;justify-content:center;font-size:9.5px;font-weight:700}
  .card-1{left:71px}.card-2{left:226px}.card-3{left:382px}.card-4{left:536px}
  .img-surveillance{background:linear-gradient(180deg,#c9dff1,#9fb6c8)}
  .img-weapons{background:linear-gradient(180deg,#d8d8d8,#3a3d42 60%,#2a2a2a)}
  .img-vehicles{background:linear-gradient(180deg,#e3e8ec,#5e6770 60%,#cfc8bc)}
  .img-ambulances{background:linear-gradient(180deg,#b7a88c,#e9e9e9 50%,#c44a45 80%,#eeeeee)}

  /* footer */
  .site-footer{position:absolute;left:0;top:904px;width:745px;height:232px;background:var(--black)}
  .footer-brand{position:absolute;left:70px;top:30px;line-height:1}
  .footer-brand .brand-name{font-size:34px}
  .footer-brand .brand-tag{font-size:15px;letter-spacing:4px;margin-top:2px}
  .footer-about{position:absolute;left:70px;top:107px;width:190px;font-size:8px;line-height:13px;font-weight:700}
  .footer-links{position:absolute;left:360px;top:37px;list-style:none;font-size:8px;font-weight:700;line-height:14px}
  .footer-links li::before{content:"";display:inline-block;width:4px;height:4px;border-radius:50%;background:var(--blue);margin-right:5px;vertical-align:middle}
  .contact-list{position:absolute;left:574px;top:32px;list-style:none;font-size:8px;font-weight:700;line-height:13px}
  .contact-item{position:relative;padding-left:22px}
  .contact-item svg{position:absolute;left:0;top:0}
  .ci-address{height:50px}.ci-email{height:35px}
  .footer-rule{position:absolute;left:70px;top:194px;width:606px;height:1px;background:var(--rule)}
  .copyright{position:absolute;left:0;width:100%;top:208px;text-align:center;font-size:8px;font-weight:700}
  .copyright a{color:var(--blue-soft);text-decoration:none}
</style>
</head>
<body>
<div class="page">
  <header class="site-header">
    <div class="brand"><span class="brand-name">VEMRA</span><span class="brand-tag">SECURITY</span></div>
    <nav class="main-nav">
      <a href="#">Home</a>
      <a href="#" class="is-active">About Us</a>
      <a href="#">Guyana Security Overview</a>
      <a href="#">Services</a>
      <a href="#">Contact Us</a>
    </nav>
  </header>

  <section class="page-hero" role="img" aria-label="Blue-toned photo of a security officer in a suit outside a glass building">
    <h1 class="page-title">ABOUT US</h1>
    <div class="title-rule"></div>
  </section>

  <h2 class="intro-heading">When security is concerned, we never take it lightly!</h2>
  <div class="intro-copy">
    <p>VEMRA Security teams are fully licensed by the Guyanese Police Force to offer armed and unarmed security services and all service weapons and ammunition are controlled and maintained in full compliance with Guyanese regulations.</p>
    <p>VEMRA's British Operatives are all highly trained former elite military personnel or former Police and Securities Industry Association (SIA) licensed security operatives. All Guyanese operatives have been through the same training as would be expected to qualify for SIA or Northgate CP Licenses (and Guyanese accreditation is being sought).</p>
    <p>Our in-country assets include trained personnel (Guyanese and British Elite Services), modern weapons, advanced tracking and surveillance equipment, three fully equipped ambulances, heliport, private indoor training gallery.</p>
    <p>All operations are monitored constantly from Operations Control Rooms in Guyana and the UK.</p>
    <p>A full due diligence pack providing details of our Principals, Licences and Permits will be provided in response to any Request For Proposal.</p>
  </div>
  <div class="intro-photo" role="img" aria-label="Photo of a uniformed security officer in a dark uniform standing outdoors"></div>

  <h2 class="section-title">OUR ASSETS</h2>
  <div class="section-rule"></div>

  <article class="asset-card card-1">
    <div class="asset-image img-surveillance" role="img" aria-label="Photo of a wall-mounted surveillance camera"></div>
    <div class="asset-label">Surveillance Equipment</div>
  </article>
  <article class="asset-card card-2">
    <div class="asset-image img-weapons" role="img" aria-label="Photo of an armed guard in a protective vest holding a weapon"></div>
    <div class="asset-label">Modern Weapons</div>
  </article>
  <article class="asset-card card-3">
    <div class="asset-image img-vehicles" role="img" aria-label="Photo of an open-top four-wheel-drive vehicle"></div>
    <div class="asset-label">4WD Vehicles</div>
  </article>
  <article class="asset-card card-4">
    <div class="asset-image img-ambulances" role="img" aria-label="Photo of a white and red ambulance"></div>
    <div class="asset-label">Ambulances</div>
  </article>

  <footer class="site-footer">
    <div class="footer-brand"><span class="brand-name">VEMRA</span><span class="brand-tag">SECURITY</span></div>
    <p class="footer-about">VEMRA is a Trading Division of Berbice Crest Developments Inc, a duly incorporated and registered Guyanese corporation with Company Registration Number XXXXX and located at XXXXXXXXX.</p>
    <ul class="footer-links">
      <li>Home</li><li>About Us</li><li>Guyana Security Overview</li><li>Services</li><li>Contact Us</li><li>Useful Links</li>
    </ul>
    <ul class="contact-list">
      <li class="contact-item ci-address">
        <svg width="14" height="16" viewBox="0 0 14 16"><path d="M7 0C3.4 0 1 2.6 1 5.8 1 10 7 16 7 16s6-6 6-10.2C13 2.6 10.6 0 7 0z" fill="var(--blue)"/><circle cx="7" cy="5.8" r="2.2" fill="var(--black)"/></svg>
        214 Canal Street<br>Tucson, AZ 85701
      </li>
      <li class="contact-item ci-email">
        <svg width="16" height="14" viewBox="0 0 16 14"><path d="M0 6 16 0 12 14 7 9 12 3 5 8z" fill="var(--blue)"/></svg>
        ba@vemra.group
      </li>
      <li class="contact-item">
        <svg width="15" height="15" viewBox="0 0 15 15"><path d="M3 0 6 4 4.5 6C5.5 8 7 9.5 9 10.5L11 9l4 3-2 3C6 14.5.5 9 0 2z" fill="var(--blue)"/></svg>
        +1 (206) 555-0142
      </li>
    </ul>
    <div class="footer-rule"></div>
    <p class="copyright">© 2020 VEMRA. All Rights Reserved. <a href="#">Terms</a>. <a href="#">Privacy Policy</a>.</p>
  </footer>
</div>
</body>
</html>
```